MORIVO VEGAN SUSHI

www.morivo-restaurant.de
We are open in 2018 and are an innovative restaurant from Munich. We would like a cool design for our drinks and food menu. It's very simple at the moment. See the File menu. In any case, our logo should appear. On the website we use neutraface as a font. But it's not a must. We are only open in the evening and appeal to a young, upscale audience.

```html
<!DOCTYPE html>
<html lang="de">
<head>
<meta charset="utf-8">
<title>MORIVO – Speisekarte</title>
<link rel="stylesheet" href="https://fonts.googleapis.com/css2?family=Josefin+Sans:wght@300;400;700&display=swap">
<style>
  :root {
    --ink: #333333;
    --ink-soft: #4a4a4a;
    --panel: #dcdcdc;
    --slogan: #8c8c8c;
    --paper: #ffffff;
    --rule: #3a3a3a;
  }
  * { box-sizing: border-box; margin: 0; padding: 0; }
  html, body { width: 848px; height: 1200px; overflow: hidden; background: var(--paper); }
  body { font-family: "Josefin Sans", sans-serif; color: var(--ink); position: relative; font-weight: 300; }

  .brand { position: absolute; left: 0; width: 620px; top: 36px; text-align: center; }
  .brand-dot { width: 86px; height: 86px; border-radius: 50%; background: var(--ink); margin: 0 auto 32px; }
  .brand-name { font-size: 21px; font-weight: 300; letter-spacing: 17px; padding-left: 17px; }

  .menu-section { position: absolute; left: 61px; width: 476px; }
  .section-title { font-weight: 700; font-size: 15px; height: 20px; line-height: 22px; letter-spacing: 0.3px; }
  .dish { display: flex; align-items: baseline; height: 22.4px; line-height: 24px; font-size: 13.5px; white-space: nowrap; }
  .dish small { font-size: 12.5px; }
  .dish .leader { flex: 1; border-bottom: 1px dotted var(--ink-soft); margin: 0 2px; transform: translateY(-3px); }
  .dish.two-line { height: auto; line-height: 14.5px; padding-bottom: 6px; display: block; }
  .dish.two-line .row { display: flex; align-items: baseline; }

  .footer { position: absolute; left: 55px; width: 479px; text-align: center; }
  .footer-note { top: 1050px; font-size: 12.5px; line-height: 15px; }
  .footer-note p + p { margin-top: 7px; }
  .footer-rule { top: 1116px; border-top: 1px solid var(--rule); }
  .footer-contact { top: 1134px; left: 55px; width: 490px; font-size: 11.5px; line-height: 15px; }
  .footer-contact .web { font-weight: 700; font-size: 10.5px; letter-spacing: 0.3px; }

  .offer-panel { position: absolute; left: 560px; top: 20px; width: 270px; height: 1162px; background: var(--panel); }
  .slogan { position: absolute; left: 19px; top: 64px; font-size: 30px; line-height: 31px; color: var(--slogan); font-weight: 300; text-transform: uppercase; }

  .offer { position: absolute; left: 19px; width: 210px; }
  .offer-title { font-weight: 700; font-size: 15px; height: 18px; line-height: 20px; }
  .offer-title small { font-size: 13.5px; }
  .offer-sub { font-style: italic; font-size: 11px; height: 14px; line-height: 15px; }
  .offer-list { list-style: none; font-size: 13.5px; }
  .offer-list li { position: relative; padding-left: 12px; line-height: 21.2px; height: 21.2px; white-space: nowrap; }
  .offer-list li::before { content: "·"; position: absolute; left: 0; }
  .offer-list li.tall { height: auto; line-height: 17px; padding-top: 2px; padding-bottom: 3px; }
  .offer-list small { font-size: 12.5px; }
  .offer-price { font-weight: 700; font-size: 13.5px; line-height: 22px; padding-top: 3px; padding-bottom: 2px; border-bottom: 1px dotted var(--ink-soft); }
</style>
</head>
<body>

  <header class="brand">
    <div class="brand-dot"></div>
    <div class="brand-name">MORIVO</div>
  </header>

  <section class="menu-section" style="top:229px">
    <h2 class="section-title">VORSPEISEN</h2>
    <div class="dish">MISO SUPPE<span class="leader"></span>5,50€</div>
    <div class="dish">EDAMAME MIT SALZ/CHILI<span class="leader"></span>4,50€</div>
    <div class="dish">SEIDENTOFU&nbsp;<small>in hausgemachter Sauce mit Mandeln</small><span class="leader"></span>5,50€</div>
  </section>

  <section class="menu-section" style="top:351px">
    <h2 class="section-title">SUSHI</h2>
    <div class="dish">URAMAKI&nbsp;<small>mit Tempuragemüse</small><span class="leader"></span>8,90€</div>
    <div class="dish">FUTOMAKI&nbsp;<small>wechselndes Gemüse</small><span class="leader"></span>8,00€</div>
    <div class="dish">URAMAKI&nbsp;<small>mit Austernpilze</small><span class="leader"></span>7,50€</div>
    <div class="dish">HOSOMAKI&nbsp;<small>Gurke Avocado</small><span class="leader"></span>5,50€</div>
    <div class="dish">HOSOMAKI&nbsp;<small>Gurke Shiitake</small><span class="leader"></span>5,50€</div>
    <div class="dish">TOMATEN NIGIRI<span class="leader"></span>4,50€</div>
  </section>

  <section class="menu-section" style="top:539px">
    <h2 class="section-title">KLEINE GERICHTE</h2>
    <div class="dish">GEMÜSE TEMPURA<span class="leader"></span>8,00 €</div>
    <div class="dish"><small>Crispy</small>&nbsp;TOFUSTICKS&nbsp;<small>mit Mayo</small><span class="leader"></span>8,00€</div>
    <div class="dish">KÜRBISKROKETTEN&nbsp;<small>mit</small>&nbsp;TANGASHU<span class="leader"></span>7,90€</div>
    <div class="dish">SUSHI “THUNA” CAKE<span class="leader"></span>6,90€</div>
    <div class="dish">SUSHI CAKE CLASSIC<span class="leader"></span>6,00€</div>
    <div class="dish">AUBERGINE DENGAKU<span class="leader"></span>5,50€</div>
  </section>

  <section class="menu-section" style="top:728px">
    <h2 class="section-title">HAUPTSPEISEN</h2>
    <div class="dish two-line">
      <div><small>Herrlich cremiges</small> KATSU CURRY</div>
      <div class="row"><small>mit knusprigen Auberginensticks, Reis &amp; Pickles</small><span class="leader"></span>17,90€</div>
    </div>
    <div class="dish">RAMEN SUPPE&nbsp;<small>mit Nudeln, Gemüse &amp; Tofu</small><span class="leader"></span>14,90€</div>
    <div class="dish">CHIRASHI SUSHI BOWL<span class="leader"></span>13,90€</div>
    <div class="dish">SOMMERSALATE&nbsp;<small>mit Sesamdressing &amp; crispy Tofusticks mit Mayo</small><span class="leader"></span>12,50€</div>
  </section>

  <section class="menu-section" style="top:886px">
    <h2 class="section-title">DESSERT</h2>
    <div class="dish">CHEESECAKE&nbsp;<small>mit Beeren</small><span class="leader"></span>6,50€</div>
    <div class="dish">PANA COTTA&nbsp;<small>mit Beeren</small><span class="leader"></span>5,90€</div>
    <div class="dish">SORBET&nbsp;<small>des Tages</small><span class="leader"></span>5,50€</div>
    <div class="dish">SORBET&nbsp;<small>des Tages mit Schuss</small><span class="leader"></span>6,90€</div>
  </section>

  <div class="footer footer-note">
    <p>All vegan</p>
    <p>Bitte teilen Sie dem Service unbedingt Allergien mit und<br>fragen Sie nach der Allergiker-Menükarte</p>
  </div>
  <div class="footer footer-rule"></div>
  <footer class="footer footer-contact">
    <p>Mo-Sa: 17:30h-22h • 089 | 123456780 • Lindenweg 12, 80802 München</p>
    <p class="web">www.morivo-restaurant.de</p>
  </footer>

  <aside class="offer-panel">
    <p class="slogan">Pures<br>Glück<br>zu jeder<br>Saison.</p>

    <div class="offer" style="top:211px">
      <h3 class="offer-title">CHEF MENÜ <small>mit Aperitiv</small></h3>
      <p class="offer-sub">für 2 Personen</p>
      <ul class="offer-list">
        <li class="tall"><small>Kleine Portion</small> RAMENSUPPE<br><small>mit Gemüse &amp; Nudeln</small></li>
        <li>MINI SET</li>
        <li style="margin-top:3px">DESSERT</li>
      </ul>
      <p class="offer-price">81,00€</p>
    </div>

    <div class="offer" style="top:372px">
      <h3 class="offer-title">OMAKASE</h3>
      <p class="offer-sub">für 2 Personen</p>
      <ul class="offer-list">
        <li>EDAMAME</li>
        <li class="tall">OMAKASE SET<br><small>mit 8 Spezialitäten des Hauses</small></li>
        <li>PANA COTTA <small>mit Beeren</small></li>
      </ul>
      <p class="offer-price">68,00€</p>
    </div>

    <div class="offer" style="top:531px">
      <h3 class="offer-title">SET 1</h3>
      <ul class="offer-list">
        <li>HOSOMAKI</li>
        <li>FUTOMAKI</li>
        <li>NIGIRI</li>
        <li>KÜRBISKROKETTEN</li>
        <li>WAKAME GURKEN SALAT</li>
        <li>PICKLES</li>
        <li>GYOZA TEIGTASCHEN</li>
        <li>SUSHI CAKE</li>
      </ul>
      <p class="offer-price">33,90€</p>
    </div>

    <div class="offer" style="top:765px">
      <h3 class="offer-title">SET 2</h3>
      <ul class="offer-list">
        <li>HOSOMAKI</li>
        <li>FUTOMAKI</li>
        <li>PICKLES</li>
        <li>SUSHI “THUNA” CAKE</li>
        <li><small>Crispy</small> AUBERGINEN <small>mit</small> Mayo</li>
        <li>AUBERGINE DENGAKU</li>
      </ul>
      <p class="offer-price">31,90€</p>
    </div>

    <div class="offer" style="top:956px">
      <h3 class="offer-title">SET 3</h3>
      <ul class="offer-list">
        <li>HOSOMAKI</li>
        <li>URAMAKI</li>
        <li>NIGIRI</li>
        <li>GEMÜSE TEMPURA</li>
        <li><small>Crispy</small> TOFUSTICKS <small>mit</small> Mayo</li>
        <li>WAKAME SHIRA AE</li>
      </ul>
      <p class="offer-price">28,90€</p>
    </div>
  </aside>

</body>
</html>
```